New business needs a slick but classy, conservative and elegant Legal Letterhead

We need a new letterhead for a law firm that is slick but very classy and also understated.

The name of the firm is K.L. Marlow Lawyers.

All information about the Law firm should appear at the top of the page. Please no firm information in the footer.

It should have a clean, neat look. No watermarks or bold graphics please.

Info should include the name of the law firm, both the street address and postal address, the phone number and the fax number, the names of the principals, the website. We have attached a word document that contains the relevant information.

We have attached a copy of the business card for further information purposes.

We also need a law society logo to appear (probably on the bottom right hand side of the letterhead?) that states our affiliation to the law society. It is attached and must not be altered in any way. It can be small.

The only footer text we require is as worded in the attached information document.

We would like to see designs that use red and white - in an understated, elegant style - not too modern or too gaudy looking.

The final design should communicate that we mean business and that we are to be trusted.
Updates

Please insert firm's name K.L. Marlow Lawyers on letterhead! I have removed KLM logo as designers were using it instead of the name of the firm. Thank you!

Industry/Entity Type

Legal

Font styles to use
Serif

Colors
ec1f27
ffffff

Requirements
Must have
• All information contained in the word document attached - firm details, law society affiliation logo, firm name & firm logo, principals' names.
Should not have
• watermarks
• no firm details in footer

```html
<!DOCTYPE html>
<html lang="en">
<head>
<meta charset="utf-8">
<title>K.L. Marlow Lawyers – Letterhead</title>
<link href="https://fonts.googleapis.com/css2?family=Libre+Baskerville:wght@400;700&family=Open+Sans:wght@400;600;700&display=swap" rel="stylesheet">
<style>
  :root {
    --brand-red: #ec1f27;
    --paper: #ffffff;
    --ink: #3a3a3a;
    --badge-orange: #e8893a;
  }
  html, body {
    margin: 0;
    padding: 0;
    overflow: hidden;
    background: var(--paper);
  }
  .letterhead {
    position: relative;
    width: 849px;
    height: 1200px;
    background: var(--paper);
    overflow: hidden;
    font-family: "Open Sans", Arial, sans-serif;
    color: var(--ink);
  }
  .label {
    display: block;
    color: var(--brand-red);
    font-weight: 700;
    font-size: 10.5px;
    line-height: 14px;
  }
  .detail {
    font-size: 10.5px;
    line-height: 14px;
    margin: 0;
  }
  .addresses {
    position: absolute;
    left: 56px;
    top: 50px;
    width: 240px;
  }
  .addresses .block + .block { margin-top: 16px; }
  .firm-name {
    position: absolute;
    left: 320px;
    top: 42px;
    width: 206px;
    height: 38px;
    box-sizing: border-box;
    padding: 0 8px;
    border: 2px solid var(--brand-red);
    border-radius: 3px;
    display: flex;
    align-items: center;
    justify-content: center;
    font-family: "Libre Baskerville", Georgia, serif;
    font-weight: 700;
    font-size: 12.5px;
    letter-spacing: 0.2px;
    color: var(--brand-red);
    white-space: nowrap;
  }
  .contact {
    position: absolute;
    left: 686px;
    top: 50px;
    width: 150px;
  }
  .contact-row {
    font-size: 10.5px;
    line-height: 15px;
    margin: 0;
    white-space: nowrap;
  }
  .contact-row .key {
    color: var(--brand-red);
    font-weight: 700;
    margin-right: 6px;
  }
  .principals { margin-top: 12px; }
  .footer-note {
    position: absolute;
    left: 56px;
    top: 1136px;
    font-size: 10.5px;
    font-weight: 600;
    color: #222;
    white-space: nowrap;
  }
  .affiliation-badge {
    position: absolute;
    left: 694px;
    top: 1112px;
  }
</style>
</head>
<body>
<div class="letterhead">
  <div class="addresses">
    <div class="block">
      <span class="label">Street Address:</span>
      <p class="detail">Shop 1, 23-25 Ashgrove Circuit,<br>Parkdale North, NSW 2225</p>
    </div>
    <div class="block">
      <span class="label">Postal Address:</span>
      <p class="detail">PO Box 7310,<br>Parkdale North, NSW 2225</p>
    </div>
  </div>

  <div class="firm-name">K.L. MARLOW LAWYERS</div>

  <div class="contact">
    <p class="contact-row"><span class="key">[T]</span>(02) 9000 0101</p>
    <p class="contact-row"><span class="key">[F]</span>(02) 9000 0102</p>
    <p class="contact-row"><span class="key">[W]</span>www.klmarlow.com.au</p>
    <div class="principals">
      <span class="label">Principals:</span>
      <p class="detail">Kieran Marlow<br>Lena Marlow</p>
    </div>
  </div>

  <div class="footer-note">Liability limited by a scheme approved under Professional Standards</div>

  <svg class="affiliation-badge" width="110" height="50" viewBox="0 0 110 50" role="img" aria-label="Law society affiliation badge">
    <rect x="0" y="0" width="46" height="50" rx="6" fill="var(--badge-orange)"/>
  </svg>
</div>
</body>
</html>
```